RJK Entertainment

Logo for business card design

Target Market(s)

potential film investors and screenwriters

Industry/Entity Type

Business

Contact Information for Business Card

as shown, website here is a placeholder position

Requirements
Must have
• great visual appeal
Nice to have
• harmony of colors; must evoke spirit of
• U.S.-China cooperation

```html
<!DOCTYPE html>
<html lang="en">
<head>
<meta charset="utf-8">
<title>RJK Entertainment Business Card</title>
<link rel="stylesheet" href="https://fonts.googleapis.com/css2?family=Open+Sans:wght@400;600;700&display=swap">
<style>
  :root {
    --backdrop: #8c8c8e;
    --card-front: #e9eaed;
    --card-back: #8e8f92;
    --ink: #1e1e1e;
    --accent-red: #c8111f;
    --rule-blue: #1a237e;
    --brand-navy: #1a1f7a;
    --brand-light: #e3e8ee;
  }
  * { margin: 0; padding: 0; box-sizing: border-box; }
  html, body {
    width: 1105px;
    height: 1200px;
    overflow: hidden;
    background: var(--backdrop);
    font-family: "Open Sans", Arial, sans-serif;
  }
  .canvas {
    position: relative;
    width: 1105px;
    height: 1200px;
  }
  .card {
    position: absolute;
    left: 182px;
    width: 747px;
    height: 427px;
  }
  .card--front { top: 119px; background: var(--card-front); }
  .card--back { top: 635px; background: var(--card-back); }

  .contact {
    position: absolute;
    left: 39px;
    top: 38px;
    color: var(--ink);
    font-size: 19px;
    line-height: 1.45;
  }
  .contact__name {
    color: var(--accent-red);
    font-size: 26px;
    font-weight: 600;
    line-height: 1.2;
    margin-bottom: 4px;
  }
  .contact__title { margin-bottom: 0; }
  .contact__email { padding-left: 3px; }
  .contact__rule {
    width: 200px;
    height: 0;
    border-top: 2px dotted var(--rule-blue);
    margin: 16px 0 18px;
  }
  .contact__phones { line-height: 1.5; }
  .contact__label {
    color: var(--accent-red);
    font-weight: 700;
    margin-right: 4px;
  }

  .brand {
    position: absolute;
    display: flex;
    align-items: center;
    gap: 12px;
    font-size: 30px;
    font-weight: 700;
    white-space: nowrap;
  }
  .brand__mark {
    width: 26px;
    height: 26px;
    flex: none;
  }
  .brand--front {
    left: 372px;
    top: 191px;
    color: var(--brand-navy);
  }
  .brand--front .brand__mark { background: var(--accent-red); }
  .brand--back {
    left: 50%;
    top: 50%;
    transform: translate(-50%, -50%);
    color: var(--brand-light);
  }
  .brand--back .brand__mark { background: var(--accent-red); }
</style>
</head>
<body>
<main class="canvas">
  <section class="card card--front" aria-label="Card front">
    <div class="contact">
      <p class="contact__name">Daniel Reyes</p>
      <p class="contact__title">CEO/Founder</p>
      <p class="contact__email">dreyes@sitename.com</p>
      <div class="contact__rule"></div>
      <p>4120 Willow Court</p>
      <p>Fairbanks, Alaska 99701</p>
      <p>www.sitename.com</p>
      <div class="contact__rule"></div>
      <div class="contact__phones">
        <p><span class="contact__label">P :</span>555 214 7031</p>
        <p><span class="contact__label">F :</span>555 308 4622</p>
        <p><span class="contact__label">M :</span>555 214 7032</p>
      </div>
    </div>
    <div class="brand brand--front">
      <span class="brand__mark"></span>
      <span class="brand__name">RJK Entertainment</span>
    </div>
  </section>

  <section class="card card--back" aria-label="Card back">
    <div class="brand brand--back">
      <span class="brand__mark"></span>
      <span class="brand__name">RJK Entertainment</span>
    </div>
  </section>
</main>
</body>
</html>
```